TJ&R Roofing Billboard Design

Looking for a fresh new billboard design with my new headshot photo and using some info from my previous billboard and maybe website for design/content inspiration. My website is https://tjrroofing-example.com/

Also attached are my logo and current lawn sign design. I am looking for something simple, clean and modern. The landing page website should be 3182roof-example.com like my previous billboard has.

```html
<!DOCTYPE html>
<html lang="en">
<head>
<meta charset="utf-8">
<title>TJ&amp;R Roofing Billboard</title>
<link href="https://fonts.googleapis.com/css2?family=Poppins:wght@600;700;800&display=swap" rel="stylesheet">
<style>
  :root {
    --navy: #0b1d3b;
    --lime: #94aa38;
    --sky: #6cb4dc;
    --white: #ffffff;
    --photo-top: #e2e2e4;
    --photo-mid: #d3d8e8;
    --photo-low: #bcc6e2;
    --page: #eef1f5;
  }
  html, body {
    margin: 0;
    width: 1200px;
    height: 966px;
    overflow: hidden;
    background: var(--page);
  }
  .billboard {
    position: absolute;
    left: 0;
    top: 216px;
    width: 1200px;
    height: 535px;
    display: block;
  }
  .billboard text { font-family: "Poppins", sans-serif; }
  .company-name { fill: var(--lime); font-weight: 600; font-size: 52px; }
  .headline-main { fill: var(--white); font-weight: 800; font-size: 122px; }
  .headline-sub { fill: var(--white); font-weight: 700; font-size: 84px; }
  .price-lead { fill: var(--navy); font-weight: 800; font-size: 90px; }
  .price-amount { fill: var(--white); font-weight: 800; font-size: 68px; }
  .site-url { fill: var(--white); font-weight: 700; font-size: 58px; }
  .badge-name { fill: var(--navy); font-weight: 700; font-size: 34px; }
</style>
</head>
<body>
<svg class="billboard" viewBox="0 0 1578 704" xmlns="http://www.w3.org/2000/svg" aria-label="TJ&amp;R Roofing billboard">
  <defs>
    <linearGradient id="photo-fill" x1="0" y1="0" x2="0" y2="1">
      <stop offset="0" stop-color="var(--photo-top)"/>
      <stop offset="0.45" stop-color="var(--photo-mid)"/>
      <stop offset="1" stop-color="var(--photo-low)"/>
    </linearGradient>
  </defs>

  <rect class="headshot-area" x="880" y="0" width="698" height="704" fill="url(#photo-fill)" role="img" aria-label="Headshot of the owner smiling in a light blue shirt, roof of a house faint behind"/>

  <path class="accent-arc" d="M0,0 H1082 C1092,250 1010,480 910,704 H0 Z" fill="var(--lime)"/>
  <path class="main-panel" d="M0,0 H984 C1012,170 992,420 870,704 H0 Z" fill="var(--navy)"/>

  <text class="company-name" x="75" y="86">TJ&amp;R Roofing LLC</text>
  <line class="divider" x1="76" y1="124" x2="715" y2="124" stroke="var(--white)" stroke-width="2"/>
  <text class="headline-main" x="72" y="252">FULL ROOF</text>
  <text class="headline-sub" x="74" y="337">REPLACEMENTS</text>

  <path class="offer-band-edge" d="M0,416 Q380,350 800,440 L900,604 H0 Z" fill="var(--sky)"/>
  <path class="offer-band" d="M0,461 Q380,372 800,455 L915,604 H0 Z" fill="var(--lime)"/>
  <path class="footer-strip" d="M0,604 H905 L885,704 H0 Z" fill="var(--navy)"/>

  <text class="price-lead" x="107" y="531">Starting at</text>

  <text class="site-url" x="75" y="676">3182roof-example.com</text>

  <g class="price-tag" transform="rotate(20 740 555)">
    <path d="M615,495 H875 a12,12 0 0 1 12,12 V603 a12,12 0 0 1 -12,12 H615 L585,555 Z" fill="var(--sky)"/>
    <circle cx="612" cy="555" r="7" fill="var(--lime)"/>
    <text class="price-amount" x="748" y="578" text-anchor="middle">$7,499</text>
  </g>
  <path class="tag-string" d="M604,548 C560,560 510,565 512,548 C515,532 575,520 606,528" fill="none" stroke="var(--navy)" stroke-width="3"/>

  <g class="brand-badge">
    <circle cx="892" cy="431" r="120" fill="var(--white)" stroke="var(--sky)" stroke-width="8"/>
    <text class="badge-name" x="892" y="425" text-anchor="middle">TJ&amp;R</text>
    <text class="badge-name" x="892" y="463" text-anchor="middle">Roofing</text>
  </g>
</svg>
</body>
</html>
```